Need a new company business card

I am looking for a new company business card. Front and back. With information on it as per below. Card should be professional. Yet clever. Simple. Modern design. TUV card, traditional size. OK with say, all black or all red backside.

VorraKay is an indie, bootstrapped magazine advancing the work of intersectional feminists busting their buts to create a just world through the power of enterprise and innovation.

VorraKay is the home and voice of entrepreneurial feminism and feminist innovators worldwide. Entrepreneurial feminists are people (of all genders) who see inequality as an innovation priority. They work to advance gender equity and/or who strive to integrate and practice feminist principles, pedagogy, values into their innovation and entrepreneurship work.
We are committed to this space being trans and queer inclusive, anti-racist, intersectional, brave, and safe. We welcome all allies. We value learning, edgy but civil discourse and integrative thinking skills.

Target Market(s)

feminists, business owners,

Industry/Entity Type

Publishing Company

Contact Information for Business Card

RD Halvorn
Founder/Publisher
2-340 Pellingham Street, Toronto, ON
M4T 2K8
publisher@vorrakay.com
416-555-0143
www.vorrakay.com

Font styles to use
Serif
Other font styles liked:
• Myriad Pro

Colors
ec1f27
000000
ffffff

Requirements
Must have
• logo
• use red, black white colours only.
Nice to have
• use the compass in pattern or creatively but not too busy please
Should not have
• Should not be too busy. Elegant.

```html
<!DOCTYPE html>
<html lang="en">
<head>
<meta charset="utf-8">
<title>VorraKay — Business Card</title>
<link rel="stylesheet" href="https://fonts.googleapis.com/css2?family=Source+Sans+3:wght@400;600;700&family=Libre+Caslon+Text:ital@0;1&display=swap">
<style>
  :root {
    --red: #ec1f27;
    --black: #000000;
    --white: #ffffff;
    --ink: #2f2f2f;
    --grey: #6b6b6b;
    --pattern-light: #f4f4f4;
    --pattern-mid: #ececec;
    --backdrop: #1f2226;
    --sans: "Source Sans 3", "Myriad Pro", Arial, sans-serif;
    --serif: "Libre Caslon Text", Georgia, serif;
  }
  * { box-sizing: border-box; margin: 0; padding: 0; }
  html, body {
    width: 1200px;
    height: 900px;
    overflow: hidden;
    background: var(--backdrop);
  }
  .canvas {
    width: 1200px;
    height: 900px;
    display: flex;
    align-items: center;
    justify-content: center;
    gap: 40px;
  }
  .card {
    position: relative;
    width: 540px;
    height: 308px;
    border-radius: 22px;
    background: var(--white);
    overflow: hidden;
  }

  /* Contact side */
  .portrait-area {
    position: absolute;
    left: 96px;
    top: 22px;
    width: 240px;
    height: 128px;
    border-radius: 14px;
    background: linear-gradient(135deg, #f1f1f1 0%, #e3e3e3 70%, #f6d6d7 100%);
  }
  .address {
    position: absolute;
    left: 30px;
    top: 172px;
    font-family: var(--sans);
    font-size: 15px;
    line-height: 1.3;
    color: var(--ink);
  }
  .identity {
    position: absolute;
    right: 34px;
    top: 160px;
    text-align: right;
  }
  .identity .name {
    font-family: var(--sans);
    font-weight: 700;
    font-size: 25px;
    color: var(--red);
    line-height: 1.05;
  }
  .identity .role {
    font-family: var(--serif);
    font-size: 15px;
    letter-spacing: 0.06em;
    color: var(--grey);
    text-transform: uppercase;
  }
  .contacts {
    position: absolute;
    right: 34px;
    bottom: 26px;
    text-align: right;
    font-family: var(--sans);
    font-size: 15px;
    line-height: 1.3;
    color: var(--ink);
  }

  /* Brand side */
  .brand-side .pattern {
    position: absolute;
    inset: 0;
    background: linear-gradient(160deg, var(--pattern-light) 0%, var(--white) 45%, var(--pattern-mid) 100%);
  }
  .accent-bar {
    position: absolute;
    left: 48px;
    top: 0;
    width: 112px;
    height: 12px;
    background: var(--red);
  }
  .wordmark {
    position: absolute;
    left: 56px;
    top: 52px;
    font-family: var(--sans);
    font-weight: 700;
    font-size: 96px;
    letter-spacing: -3px;
    color: var(--ink);
    line-height: 1;
  }
  .tagline {
    position: absolute;
    left: 62px;
    top: 160px;
    font-family: var(--serif);
    font-size: 12.5px;
    letter-spacing: 0.12em;
    color: var(--ink);
    text-transform: uppercase;
  }
  .cert-badge {
    position: absolute;
    right: 44px;
    top: 150px;
    width: 24px;
    height: 24px;
    border: 2px solid var(--ink);
    border-radius: 50%;
  }
  .edge-block {
    position: absolute;
    right: 0;
    background: var(--black);
  }
  .edge-block.upper { top: 188px; width: 44px; height: 50px; }
  .edge-block.lower { top: 238px; width: 72px; height: 44px; }
</style>
</head>
<body>
  <main class="canvas">
    <section class="card contact-side" aria-label="Card contact side">
      <div class="portrait-area" role="img" aria-label="Line illustration of the founder with a speech bubble holding the brand symbol"></div>
      <p class="address">2-340 Pellingham Street<br>Toronto, ON M4T 2K8</p>
      <div class="identity">
        <p class="name">RD Halvorn</p>
        <p class="role">Founder/Publisher</p>
      </div>
      <p class="contacts">416-555-0143<br>publisher@vorrakay.com<br>www.vorrakay.com</p>
    </section>

    <section class="card brand-side" aria-label="Card brand side">
      <div class="pattern" role="img" aria-label="Faint repeating pattern of the brand symbol"></div>
      <div class="accent-bar"></div>
      <h1 class="wordmark">VorraKay</h1>
      <p class="tagline">Dispatches on Enterprise and Equity</p>
      <div class="cert-badge" role="img" aria-label="Certification badge"></div>
      <div class="edge-block upper"></div>
      <div class="edge-block lower"></div>
    </section>
  </main>
</body>
</html>
```